QRT-LM R-Value Adjustment Paper

This is a technical paper needing professional layout that is compatible with our current style guidelines; it will be used in digital and print media. It has numerous tables and graphs.

We have attached a report "QRT Cladding Dossier" issued to our company under Pellworth Certifiers graphic design guidelines. While this does NOT reflect our style branding, it does represent the 'technical' presentation we are looking for.

To view our typical company design/style please see our website at www.qrtfabric.org. Our primary RGB colors are: (187,140,9); (94,47,29); (94,138,164); and (164,167,15). Secondary RGB colors are (249,162,28) and (218,210,208). Our title/header font is DIN Next LT Pro and our copy font is Calibri 10.5 pt. We can deviate from the font specification if beneficial.

The attached file, "QRT-LM Rvalue Adj Factor" is a partial representation of the full document that will need design services. For the concepts we would like to see a cover/title page, a text/copy page and a sample of data graphic treatments.Once we have agreed upon a design concept we will determine full costs to complete the project.

Target Market(s)

Building and construction professionals, architects, building code officials

Font styles to use
Other font styles liked:
• DIN Next LT Pro

Requirements
Must have
• Design elements that help make the information easy to read and use.
Nice to have
• Right amount of white space.

```html
<!DOCTYPE html>
<html lang="en">
<head>
<meta charset="utf-8">
<title>QRT-LM Rvalue Adj Factor – Tables &amp; Graphs</title>
<link href="https://fonts.googleapis.com/css2?family=Lato:ital,wght@0,300;0,400;0,700;1,300;1,400&display=swap" rel="stylesheet">
<style>
  :root{
    --backdrop:#989898;
    --paper:#ffffff;
    --gold:#bb8c09;
    --gold-dark:#b8922e;
    --brown:#5e2f1d;
    --olive:#a4a70f;
    --eps-line:#a4ad34;
    --xps-line:#bb8c2e;
    --text:#444444;
    --muted:#8a8a8a;
    --very-cold:#8eb1e0;
    --cold:#c6d8f0;
    --hot:#fbe6d8;
    --solar:#f7b985;
    --row-a:#f4f4f4;
    --row-b:#e8e8e8;
    --band-dark:#e6e6e6;
    --band-light:#f3f3f3;
  }
  *{box-sizing:border-box;margin:0;padding:0}
  html,body{width:1200px;height:1200px;overflow:hidden;background:var(--backdrop);font-family:"Lato",sans-serif;color:var(--text)}
  .page{position:absolute;left:192px;top:72px;width:816px;height:1056px;background:var(--paper)}
  .side-rule{position:absolute;left:0;top:118px;width:18px;height:826px;background:var(--gold)}
  .page-title{position:absolute;left:66px;top:76px;font-weight:300;font-size:25px;color:var(--brown)}
  .climate-table{position:absolute;left:80px;top:182px;width:652px;border-collapse:collapse;font-size:14.5px;font-weight:300}
  .climate-table th{background:var(--gold-dark);color:#fff;font-weight:700;font-size:14px;height:37px;text-align:center}
  .climate-table th:first-child{text-align:left;padding-left:10px}
  .climate-table td{height:39px;text-align:center;color:#4a4a4a}
  .climate-table tr:nth-child(odd) td{background:var(--row-a)}
  .climate-table tr:nth-child(even) td{background:var(--row-b)}
  .climate-table td.swatch{padding:3px 5px}
  .climate-table td.swatch span{display:block;height:33px;line-height:33px}
  .very-cold span{background:var(--very-cold)}
  .cold span{background:var(--cold)}
  .hot span{background:var(--hot)}
  .solar span{background:var(--solar)}
  .caption{position:absolute;font-style:italic;font-weight:300;font-size:13px;color:#555;white-space:nowrap}
  .table-caption{left:166px;top:389px}
  .figure-caption{left:99px;top:849px}
  .chart{position:absolute;left:0;top:0;width:816px;height:1056px}
  .chart text{font-family:"Lato",sans-serif}
  .footer-name{position:absolute;left:40px;top:982px;font-size:17px;font-weight:400;color:var(--brown)}
  .footer-title{position:absolute;left:149px;top:985px;font-size:12px;font-weight:300;color:var(--muted)}
  .page-tab{position:absolute;left:664px;top:974px;width:79px;height:82px;background:var(--olive);color:#fff;text-align:center;font-weight:300}
  .page-tab .label{font-size:13px;margin-top:8px}
  .page-tab .num{font-size:16px;margin-top:2px}
  .page-tab .rev{font-size:8px;margin-top:4px}
</style>
</head>
<body>
<div class="page">
  <div class="side-rule"></div>
  <h1 class="page-title">Tables &amp; Graphs</h1>

  <table class="climate-table">
    <thead>
      <tr><th>Climate Condition</th><th>“Inside” Temp</th><th>“Outside” Temp</th><th>Temp Diff</th><th>Mean Temp</th></tr>
    </thead>
    <tbody>
      <tr><td class="swatch very-cold"><span>Very Cold</span></td><td>72°F (22°C)</td><td class="swatch very-cold"><span>0°F (-18°C)</span></td><td>72°F (40°C)</td><td>36°F (2°C)</td></tr>
      <tr><td class="swatch cold"><span>Cold</span></td><td>72°F (22°C)</td><td class="swatch cold"><span>36°F (2°C)</span></td><td>36°F (20°C)</td><td>54°F (12°C)</td></tr>
      <tr><td class="swatch hot"><span>Hot</span></td><td>72°F (22°C)</td><td class="swatch hot"><span>108°F (42°C)</span></td><td>36°F (20°C)</td><td>90°F (32°C)</td></tr>
      <tr><td class="swatch solar"><span>Solar Heated</span></td><td>72°F (22°C)</td><td class="swatch solar"><span>144°F (62°C)</span></td><td>72°F (40°C)</td><td>108°F (42°C)</td></tr>
    </tbody>
  </table>
  <p class="caption table-caption">Table 2. Mean Temperatures as a Function of Climate Condition [ CITATION BSC2 \l 1033 ]</p>

  <svg class="chart" viewBox="0 0 816 1056" aria-label="Loss of R-value versus moisture content for EPS and XPS">
    <g transform="translate(-192,-72) scale(0.8)">
      <rect x="452" y="696" width="701" height="70" fill="var(--band-dark)"/>
      <rect x="452" y="766" width="701" height="74" fill="var(--band-light)"/>
      <rect x="452" y="840" width="701" height="70" fill="var(--band-dark)"/>
      <rect x="452" y="910" width="701" height="74" fill="var(--band-light)"/>
      <rect x="452" y="984" width="701" height="74" fill="var(--band-dark)"/>
      <g stroke="#fff" stroke-width="1.5">
        <line x1="452" y1="766" x2="1153" y2="766"/><line x1="452" y1="840" x2="1153" y2="840"/>
        <line x1="452" y1="910" x2="1153" y2="910"/><line x1="452" y1="984" x2="1153" y2="984"/>
      </g>
      <line x1="452" y1="696" x2="452" y2="1058" stroke="#555" stroke-width="1.5"/>
      <line x1="452" y1="1058" x2="1153" y2="1058" stroke="#555" stroke-width="1.5"/>
      <path d="M452 1058 C560 990 700 900 800 850 S 980 760 1055 742" fill="none" stroke="var(--eps-line)" stroke-width="4.5"/>
      <path d="M452 1058 C620 990 850 910 1055 851" fill="none" stroke="var(--xps-line)" stroke-width="4.5"/>
      <g font-size="19" font-weight="300" fill="#444" text-anchor="end">
        <text x="427" y="703">25</text><text x="427" y="773">20</text><text x="427" y="848">15</text>
        <text x="427" y="918">10</text><text x="427" y="993">5</text>
      </g>
      <g font-size="19" font-weight="300" fill="#444" text-anchor="middle">
        <text x="548" y="1084">1</text><text x="648" y="1084">2</text><text x="750" y="1084">3</text>
        <text x="850" y="1084">4</text><text x="953" y="1084">5</text><text x="1053" y="1084">6</text><text x="1152" y="1084">7</text>
      </g>
      <text x="380" y="865" font-size="17" font-weight="700" fill="#222" text-anchor="middle" transform="rotate(-90 380 865)">R-value Loss, %</text>
      <text x="670" y="1122" font-size="17" font-weight="700" fill="#222" text-anchor="middle">Moisture, Vol. %</text>
      <rect x="826" y="1106" width="20" height="19" fill="var(--eps-line)"/>
      <text x="860" y="1122" font-size="17" font-weight="300" fill="#444">EPS</text>
      <rect x="943" y="1106" width="20" height="19" fill="var(--xps-line)"/>
      <text x="976" y="1122" font-size="17" font-weight="300" fill="#444">XPS</text>
    </g>
  </svg>
  <p class="caption figure-caption">Figure 4. Loss of R-value by Polystyrene Foam Insulation Due to the Absorption of moisture [ CITATION ISO07 \l 1033 ]</p>

  <p class="footer-name">QRT-LM</p>
  <p class="footer-title">Polystyrene Foam Insulation in Long-Term Building Applications – Effective R-values</p>
  <div class="page-tab">
    <div class="label">Page</div>
    <div class="num">3 of 20</div>
    <div class="rev">rev. 7-26-18</div>
  </div>
</div>
</body>
</html>
```